Bref créative
Letterhead, envelope, business card
Sunny Harbor Snackworks, LLC
Bright & Fun-filled
Daniel T. Whitcombe
Partner
4870 Lakeview Court East
Morganville, NJ 07751
dwhitcombe@sunnyharborsnackworks.com
sunnyharborsnackworks.com

```html
<!DOCTYPE html>
<html lang="en">
<head>
<meta charset="utf-8">
<title>Sunny Harbor Snackworks — Stationery</title>
<link rel="stylesheet" href="https://fonts.googleapis.com/css2?family=Lato:wght@400;700;900&display=swap">
<style>
  :root{
    --board:#ebe4d8;
    --paper:#ffffff;
    --blue:#1f4fa6;
    --red:#d7262f;
    --ink:#444a55;
    --label:#6d665c;
    --faint:rgba(31,79,166,.10);
    --shadow:0 1px 4px rgba(0,0,0,.18);
  }
  *{box-sizing:border-box;margin:0;padding:0}
  html,body{width:1200px;height:446px;overflow:hidden}
  body{background:var(--board);font-family:"Lato",sans-serif;color:var(--ink);position:relative}
  .piece{position:absolute;background:var(--paper);box-shadow:var(--shadow);overflow:hidden}
  .label{position:absolute;font-size:8px;letter-spacing:.12em;text-transform:uppercase;color:var(--label);text-align:center}
  .brand{display:flex;align-items:center;gap:4px;font-weight:900;color:var(--blue);white-space:nowrap}
  .brand .dot{border-radius:50%;background:var(--red);flex:none}
  .swoosh{position:absolute;left:0;bottom:0;width:100%}

  /* business cards */
  .card{left:19px;width:118px;height:67px}
  .card--front{top:290px}
  .card--back{top:372px}
  .card .brand{position:absolute}
  .card--front .brand{left:5px;top:8px;font-size:5px;gap:3px}
  .card--front .brand .dot{width:6px;height:6px}
  .card-details{position:absolute;left:54px;right:4px;top:8px;font-size:3px;line-height:1.45;overflow-wrap:anywhere}
  .card--back .brand{left:50%;top:22px;transform:translateX(-50%);font-size:9px}
  .card--back .brand .dot{width:10px;height:10px}
  .label--concepts{left:8px;top:200px;width:140px;text-align:left}

  /* letterheads */
  .letterhead{top:7px;width:313px;height:405px}
  .letterhead--one{left:187px}
  .letterhead--two{left:530px}
  .letterhead .brand{position:absolute;top:22px}
  .letterhead--one .brand{left:60px;font-size:9px}
  .letterhead--one .brand .dot{width:11px;height:11px}
  .letterhead--two .brand{left:58px;font-size:12px}
  .letterhead--two .brand .dot{width:14px;height:14px}
  .letterhead-contact{position:absolute;font-size:4px;line-height:1.5;text-align:left}
  .letterhead--one .letterhead-contact{left:200px;top:18px}
  .letterhead--two .letterhead-contact{left:50%;top:370px;transform:translateX(-50%);text-align:center;width:290px;font-size:4.5px}
  .watermark{position:absolute;left:50%;top:150px;transform:translateX(-50%);font-size:26px;font-weight:900;color:var(--faint);display:flex;flex-direction:column;align-items:center;gap:6px;white-space:nowrap}
  .watermark .ring{width:110px;height:110px;border-radius:50%;background:var(--faint)}
  .letterhead-footer{position:absolute;left:0;right:0;bottom:10px;text-align:center;font-size:4.5px;color:#fff}

  /* envelopes */
  .envelope{left:855px;width:333px;height:136px}
  .envelope--back{top:6px;background:var(--blue)}
  .envelope--open{top:148px}
  .envelope--front{top:278px;height:134px}
  .flap{position:absolute;left:0;top:0;width:100%;height:100%}
  .envelope--front .brand{position:absolute;left:50%;top:44px;transform:translateX(-50%);font-size:11px}
  .envelope--front .brand .dot{width:13px;height:13px}
  .envelope--open .brand{position:absolute;left:50%;top:78px;transform:translateX(-50%);font-size:10px}
  .envelope--open .brand .dot{width:12px;height:12px}
  .return-address{position:absolute;left:10px;top:8px;font-size:4px;line-height:1.5}
</style>
</head>
<body>

  <div class="label label--concepts">Background Concepts</div>

  <section class="piece card card--front" aria-label="Business card front">
    <div class="brand"><span class="dot"></span>Sunny Harbor</div>
    <div class="card-details">
      <strong>Daniel T. Whitcombe</strong><br>Partner<br>
      4870 Lakeview Court East<br>Morganville, NJ 07751<br>
      dwhitcombe@sunnyharborsnackworks.com<br>sunnyharborsnackworks.com
    </div>
    <svg class="swoosh" viewBox="0 0 118 16" height="16" aria-hidden="true">
      <path d="M0 6 Q59 16 118 4 L118 16 L0 16Z" fill="var(--red)"/>
      <path d="M0 10 Q59 18 118 8 L118 16 L0 16Z" fill="var(--blue)"/>
    </svg>
  </section>
  <div class="label" style="left:19px;top:359px;width:118px;font-size:6px">Business Card Front</div>

  <section class="piece card card--back" aria-label="Business card back">
    <div class="brand"><span class="dot"></span>Sunny Harbor</div>
    <svg class="swoosh" viewBox="0 0 118 16" height="16" aria-hidden="true">
      <path d="M0 6 Q59 16 118 4 L118 16 L0 16Z" fill="var(--red)"/>
      <path d="M0 10 Q59 18 118 8 L118 16 L0 16Z" fill="var(--blue)"/>
    </svg>
  </section>

  <section class="piece letterhead letterhead--one" aria-label="Letterhead option 1">
    <div class="brand"><span class="dot"></span>Sunny Harbor Snackworks</div>
    <div class="letterhead-contact">
      4870 Lakeview Court East<br>Morganville, NJ 07751<br>
      dwhitcombe@sunnyharborsnackworks.com<br>sunnyharborsnackworks.com
    </div>
    <div class="watermark"><span class="ring"></span>Sunny Harbor</div>
    <svg class="swoosh" viewBox="0 0 313 40" height="40" aria-hidden="true">
      <path d="M0 12 Q156 40 313 6 L313 40 L0 40Z" fill="var(--red)"/>
      <path d="M0 18 Q156 46 313 14 L313 40 L0 40Z" fill="var(--blue)"/>
    </svg>
    <div class="letterhead-footer">Sunny Harbor Snackworks, LLC · sunnyharborsnackworks.com</div>
  </section>
  <div class="label" style="left:187px;top:423px;width:313px">Letterhead Option 1</div>

  <section class="piece letterhead letterhead--two" aria-label="Letterhead option 2">
    <div class="brand"><span class="dot"></span>Sunny Harbor Snackworks</div>
    <div class="watermark"><span class="ring"></span>Sunny Harbor</div>
    <div class="letterhead-contact">
      4870 Lakeview Court East · Morganville, NJ 07751 · dwhitcombe@sunnyharborsnackworks.com · sunnyharborsnackworks.com
    </div>
    <svg class="swoosh" viewBox="0 0 313 24" height="24" aria-hidden="true">
      <path d="M0 14 Q156 28 313 10 L313 24 L0 24Z" fill="var(--red)"/>
      <path d="M0 19 Q156 30 313 16 L313 24 L0 24Z" fill="var(--blue)"/>
    </svg>
  </section>
  <div class="label" style="left:530px;top:423px;width:313px">Letterhead Option 2</div>

  <section class="piece envelope envelope--back" aria-label="Envelope back">
    <svg class="flap" viewBox="0 0 333 136" preserveAspectRatio="none" aria-hidden="true">
      <rect y="60" width="333" height="76" fill="#fff"/>
      <path d="M0 0 L333 0 L333 60 Q166 80 0 60Z" fill="var(--blue)"/>
    </svg>
  </section>

  <section class="piece envelope envelope--open" aria-label="Envelope open flap">
    <svg class="flap" viewBox="0 0 333 136" preserveAspectRatio="none" aria-hidden="true">
      <path d="M0 0 L333 0 L333 40 Q166 70 0 40Z" fill="var(--red)"/>
      <path d="M0 0 L166 52 L333 0" fill="none" stroke="#eee" stroke-width="1"/>
    </svg>
    <div class="brand"><span class="dot"></span>Sunny Harbor</div>
  </section>

  <section class="piece envelope envelope--front" aria-label="Envelope front">
    <div class="return-address">4870 Lakeview Court East<br>Morganville, NJ 07751</div>
    <div class="brand"><span class="dot"></span>Sunny Harbor Snackworks</div>
    <svg class="swoosh" viewBox="0 0 333 22" height="22" aria-hidden="true">
      <path d="M0 10 Q166 26 333 6 L333 22 L0 22Z" fill="var(--red)"/>
      <path d="M0 15 Q166 28 333 12 L333 22 L0 22Z" fill="var(--blue)"/>
    </svg>
  </section>
  <div class="label" style="left:855px;top:423px;width:333px">Envelope Option B</div>

</body>
</html>
```